Dentist's Office needs desktop and mobile website design

This is a turnkey project where we are looking for a bright, elegant, modern website design, both for desktop and mobile. Our existing website is hosted on Google sites. We also require the new design to be set up and fully functional - both desktop and mobile - on Google sites. If Google sites is too limiting, its ok to use a platform like Wix or Squarespace. If using these, we will need you to point our domain to the new Wix site, and hand us the credentials so we can continue to update the site.

We want to continue using our current logo so the new website colors need to go with the logo. Our existing website can be found at www.smilebay47.com.

We want the new website to have the following pages:
1. Home - similar content to our current home page at http://www.smilebay47.com

We also have pictures of our office and team that we would like to show up on the home page in a collage, slide show, or some other creative. Pictures can be found here: https://files.exampleshare.net/folderview?id=7KQ2MVRAXPL4hYwnBzTcLdEgHsJu&usp=sharing

Not all pictures have to be used; use as many as needed.

In addition to the content on our current home page, we would like a small section for dental quotes where we could rotate quotes. Sample quotes can be found at http://www.sayingsmeadow.net/dental.html

If above content is too much to fit on one page, it is ok to split into two.

2. Our team - similar to http://www.smilebay47.com/our-dentist-1 . In addition, we want short bios and pictures of other staff added to this page. Pictures and bios can be found here: https://files.exampleshare.net/folderview?id=7KQ2MVRAXPL4hYwnBzTcLdEgHsJu&usp=sharing

3. Reviews - similar to http://www.smilebay47.com/patient-testimonials-1

4. Services - provide a summary of services we provide from http://www.smilebay47.com/dental-services . No need for detailed pages pages for each treatment we have on our current website.

5. Contact Us - http://www.smilebay47.com/contact-us

Target Market(s)

local population

Industry/Entity Type

Healthcare

Coding

Coded - Design and coding required

Number of Pages Required

5+ page

Font styles to use
Sans Serif

Requirements
Nice to have
• animated icons would be cool

```html
<!DOCTYPE html>
<html lang="en">
<head>
<meta charset="utf-8">
<title>Bayside Dental Care</title>
<link rel="stylesheet" href="https://fonts.googleapis.com/css2?family=Roboto:wght@400;500;700&family=Open+Sans:wght@400;600&display=swap">
<style>
:root{
  --orange:#ec8a34;
  --orange-dark:#c9681e;
  --green-top:#8cbf3f;
  --green-btn:#6b9440;
  --dark:#2b2b2b;
  --darker:#232323;
  --text:#555;
  --text-dark:#333;
  --light-bg:#ececec;
  --pill:#e8e8e8;
  --white:#fff;
}
*{margin:0;padding:0;box-sizing:border-box}
html,body{width:1200px;height:2302px;overflow:hidden}
body{position:relative;background:var(--white);font-family:'Open Sans',Arial,sans-serif;color:var(--text)}
.abs{position:absolute}
.head-font{font-family:'Roboto',Arial,sans-serif}

/* header */
.top-line{left:0;top:0;width:1200px;height:3px;background:var(--green-top)}
.site-header{left:0;top:3px;width:1200px;height:149px;background:var(--white)}
.brand{left:110px;top:48px;display:flex;align-items:center;gap:12px}
.brand-mark{width:34px;height:34px;border-radius:50%;background:var(--orange)}
.brand-name{font-family:'Roboto',Arial,sans-serif;font-size:30px;font-weight:400;color:var(--orange);line-height:1}
.header-contact{right:112px;top:35px;font-size:14px;color:#666;display:flex;gap:22px;align-items:center}
.header-contact span{display:flex;align-items:center;gap:7px}
.main-nav{left:485px;top:81px;width:603px;height:53px;background:var(--darker);border-radius:27px;display:flex;align-items:center;padding:0 12px;justify-content:space-between}
.main-nav a{font-family:'Roboto',Arial,sans-serif;font-size:12px;font-weight:500;color:var(--white);text-decoration:none;padding:11px 22px;border-radius:20px;letter-spacing:.2px}
.main-nav a.active{background:var(--orange)}

/* hero */
.hero{left:0;top:152px;width:1200px;height:488px;background:linear-gradient(135deg,#cdb9a2 0%,#e6e3de 40%,#c5c2bd 70%,#9a8f84 100%)}
.hero-arrow{width:41px;height:41px;background:rgba(90,90,90,.7);top:376px;display:flex;align-items:center;justify-content:center}
.hero-caption{left:112px;background:rgba(255,255,255,.82);font-family:'Roboto',Arial,sans-serif;color:var(--text-dark);display:flex;align-items:center;padding-left:30px}
.cap-1{top:445px;width:690px;height:68px;font-size:26px}
.cap-2{top:523px;width:620px;height:62px;font-size:18px}

/* dentist */
.dark-band{left:0;top:640px;width:1200px;height:132px;background:var(--dark)}
.section-title{font-family:'Roboto',Arial,sans-serif;font-size:21px;font-weight:400}
.dentist-title{left:110px;top:674px;color:var(--white)}
.avatar{left:110px;top:721px;width:102px;height:102px;border-radius:50%;background:linear-gradient(160deg,#f0c9a8,#e07a5a);border:4px solid var(--white);box-shadow:0 1px 4px rgba(0,0,0,.3)}
.mini-arrows{left:145px;top:836px;display:flex;gap:4px}
.dot-btn{width:14px;height:14px;border-radius:50%;background:#555;display:flex;align-items:center;justify-content:center}
.dentist-name{left:227px;top:738px;font-size:13px;color:var(--orange)}
.bio{left:227px;top:790px;width:518px;font-size:11px;line-height:30.5px;color:#666;text-align:justify}
.divider-h{left:110px;top:958px;width:645px;height:1px;background:#ddd}
.perk-icon{width:70px;height:70px;border-radius:50%;border:2px solid var(--orange);top:993px;display:flex;align-items:center;justify-content:center}
.perk-small{font-family:'Roboto',Arial,sans-serif;font-size:11px;color:var(--text-dark);top:1008px}
.perk-big{font-family:'Roboto',Arial,sans-serif;font-size:17px;font-weight:700;color:var(--text-dark);top:1028px}
.perk-sep{left:430px;top:993px;width:1px;height:70px;background:#ddd}

/* hours */
.hours-card{left:780px;top:674px;width:308px;height:408px;background:var(--white);border:1px solid #ddd;box-shadow:0 2px 8px rgba(0,0,0,.12)}
.hours-head{left:0;top:0;width:306px;height:98px;background:linear-gradient(180deg,#ec8a34,#c66a22);color:var(--white);font-family:'Roboto',Arial,sans-serif;font-size:20px;text-align:center;display:flex;align-items:center;justify-content:center;line-height:30px}
.hours-row{left:23px;width:261px;height:38px;border-radius:19px;background:var(--pill);font-family:'Roboto',Arial,sans-serif;font-size:12px;color:#444;display:flex;align-items:center}
.hours-row .day{width:146px;text-align:right}
.hours-row .time{margin-left:26px}
.appt-btn{left:25px;top:334px;width:256px;height:49px;border-radius:25px;background:linear-gradient(180deg,#7fa84c,#5a8233);color:var(--white);font-family:'Roboto',Arial,sans-serif;font-size:15px;display:flex;align-items:center;justify-content:center}

/* services */
.services{left:0;top:1131px;width:1200px;height:331px;background:var(--light-bg)}
.services-title{left:110px;top:1170px;font-size:26px;color:var(--text-dark)}
.svc-arrows{left:1043px;top:1179px;display:flex;gap:6px}
.svc-arrows .dot-btn{width:19px;height:19px}
.svc-photo{top:1237px;width:219px;height:144px;border:3px solid var(--white);box-shadow:0 1px 3px rgba(0,0,0,.15)}
.svc-label{top:1398px;font-size:12px;color:#555}

/* testimonials */
.testimonials{left:0;top:1462px;width:1200px;height:277px;background:linear-gradient(90deg,rgba(232,133,52,.93),rgba(236,142,62,.9)),linear-gradient(#6b4a2e,#3a2a1c)}
.testi-title{left:0;top:1508px;width:1200px;text-align:center;font-size:26px;color:var(--white)}
.testi-quote{left:140px;top:1562px;width:920px;text-align:center;font-size:12px;line-height:25px;color:var(--white)}
.testi-name{left:0;top:1633px;width:1200px;text-align:center;font-family:'Roboto',Arial,sans-serif;font-size:14px;color:var(--white)}
.testi-dots{left:582px;top:1666px;display:flex;gap:4px}
.testi-dots .dot-btn{background:var(--white)}

/* quote band */
.quote-band{left:0;top:1739px;width:1200px;height:224px;background:linear-gradient(90deg,#2e2620,#3d332b 50%,#2a231d)}
.quote-mark{left:575px;top:1800px}
.quote-text{left:0;top:1866px;width:1200px;text-align:center;font-size:16px;color:var(--white)}

/* footer */
.foot-head{top:2010px;font-family:'Roboto',Arial,sans-serif;font-size:17px;color:var(--text-dark)}
.foot-links{top:2050px;font-size:12px;line-height:30.7px;color:#555;list-style:none}
.foot-sep{top:2018px;width:1px;height:161px;background:#ddd}
.foot-org{left:483px;top:2062px;font-family:'Roboto',Arial,sans-serif;font-size:14px;font-weight:500;color:var(--text-dark)}
.foot-line{left:483px;font-size:12px;color:#555}
.badge{background:#d9dde2;border-radius:4px}
.bottom-bar{left:0;top:2225px;width:1200px;height:77px;background:var(--dark)}
.copyright{left:110px;top:2253px;font-size:12px;color:var(--white)}
.social{left:1022px;top:2254px;display:flex;gap:12px}
.social span{width:14px;height:14px;border-radius:50%;background:var(--white)}
</style>
</head>
<body>

<div class="abs top-line"></div>
<header class="abs site-header"></header>
<div class="abs brand"><span class="brand-mark"></span><span class="brand-name">Bayside Dental Care</span></div>
<div class="abs header-contact">
  <span><svg width="10" height="14" viewBox="0 0 10 14"><path d="M5 0a5 5 0 0 0-5 5c0 4 5 9 5 9s5-5 5-9a5 5 0 0 0-5-5zm0 7a2 2 0 1 1 0-4 2 2 0 0 1 0 4z" fill="#ec8a34"/></svg>4820 W Harbor Ave, Millbrook, CA 95012</span>
  <span><svg width="12" height="12" viewBox="0 0 12 12"><path d="M2.5 0.5l2 2.5-1.2 1.5a7 7 0 0 0 4.2 4.2L9 7.5l2.5 2-1.5 2C5 11.5.5 7 .5 2z" fill="#ec8a34"/></svg>555-014-2298</span>
</div>
<nav class="abs main-nav">
  <a class="active" href="#">HOME</a><a href="#">OUR TEAM</a><a href="#">REVIEWS</a><a href="#">SERVICES</a><a href="#">CONTACT US</a>
</nav>

<section class="abs hero" role="img" aria-label="Close-up photo of dental treatment equipment in the office"></section>
<div class="abs hero-arrow" style="left:23px"><svg width="12" height="18" viewBox="0 0 12 18"><path d="M9 2L3 9l6 7" stroke="#fff" stroke-width="1.5" fill="none"/></svg></div>
<div class="abs hero-arrow" style="left:1132px"><svg width="12" height="18" viewBox="0 0 12 18"><path d="M3 2l6 7-6 7" stroke="#fff" stroke-width="1.5" fill="none"/></svg></div>
<div class="abs hero-caption cap-1">IF YOU LISTEN TO OUR PATIENTS THEY WILL TELL YOU...</div>
<div class="abs hero-caption cap-2">IT'S OUR GENUINE CARE AND GENTLE NATURE THAT SETS US APART!</div>

<div class="abs dark-band"></div>
<h2 class="abs section-title dentist-title">OUR DENTIST</h2>
<div class="abs avatar" role="img" aria-label="Portrait photo of the dentist"></div>
<div class="abs mini-arrows">
  <span class="dot-btn"><svg width="6" height="8" viewBox="0 0 6 8"><path d="M4.5 1L1.5 4l3 3" stroke="#fff" stroke-width="1.5" fill="none"/></svg></span>
  <span class="dot-btn"><svg width="6" height="8" viewBox="0 0 6 8"><path d="M1.5 1l3 3-3 3" stroke="#fff" stroke-width="1.5" fill="none"/></svg></span>
</div>
<div class="abs dentist-name">Dr Mira Selwyn</div>
<p class="abs bio">Dr Mira Selwyn truly believes that a real smile comes from within, but she can help unlock it!<br>She is all about passion and compassion. A passion for dentistry and compassion for the patients is what you will experience when you visit our office. She combines many years of experience in the dental field, with her gentle and friendly personality. She likes to provide the best care to her patients, and will go the extra mile to ensure that.</p>
<div class="abs divider-h"></div>
<div class="abs perk-icon" style="left:112px"><svg width="24" height="26" viewBox="0 0 24 26"><circle cx="12" cy="7" r="6" fill="#ec8a34"/><path d="M1 26c0-7 5-11 11-11s11 4 11 11z" fill="#ec8a34"/></svg></div>
<div class="abs perk-small" style="left:200px">FREE EXAM AND CONSULTATION FOR</div>
<div class="abs perk-big" style="left:200px">NON-INSURED PATIENTS!</div>
<div class="abs perk-sep"></div>
<div class="abs perk-icon" style="left:450px"><svg width="28" height="24" viewBox="0 0 28 24"><rect x="1" y="5" width="26" height="18" rx="3" fill="none" stroke="#ec8a34" stroke-width="2"/><path d="M10 5V2h8v3" fill="none" stroke="#ec8a34" stroke-width="2"/><path d="M14 9v10M9 14h10" stroke="#ec8a34" stroke-width="3"/></svg></div>
<div class="abs perk-small" style="left:539px">FREE EXAM AND CONSULTATION FOR</div>
<div class="abs perk-big" style="left:539px">INSURED PATIENTS!</div>

<aside class="abs hours-card">
  <div class="abs hours-head">WEEKEND &amp; EMERGENCY<br>APPOINTMENTS</div>
  <div class="abs hours-row" style="top:117px"><span class="day">MONDAY&nbsp; - THURSDAY</span><span class="time">9AM - 6PM</span></div>
  <div class="abs hours-row" style="top:169px"><span class="day">FRIDAY</span><span class="time">CLOSED</span></div>
  <div class="abs hours-row" style="top:221px"><span class="day">SATURDAY</span><span class="time">8AM - 3PM</span></div>
  <div class="abs hours-row" style="top:273px"><span class="day">SUNDAY</span><span class="time">CLOSED</span></div>
  <div class="abs appt-btn">MAKE AN APPOINTMENT</div>
</aside>

<section class="abs services"></section>
<h2 class="abs section-title services-title">OUR SERVICES</h2>
<div class="abs svc-arrows">
  <span class="dot-btn"><svg width="8" height="10" viewBox="0 0 8 10"><path d="M6 1L2 5l4 4" stroke="#fff" stroke-width="2" fill="none"/></svg></span>
  <span class="dot-btn"><svg width="8" height="10" viewBox="0 0 8 10"><path d="M2 1l4 4-4 4" stroke="#fff" stroke-width="2" fill="none"/></svg></span>
</div>
<div class="abs svc-photo" style="left:112px;background:linear-gradient(135deg,#c9b5a4,#8a6e5c)" role="img" aria-label="Photo of a hygienist performing an exam and cleaning"></div>
<div class="abs svc-photo" style="left:364px;background:linear-gradient(135deg,#b8a898,#4a4440)" role="img" aria-label="Photo of a dentist placing a tooth colored filling"></div>
<div class="abs svc-photo" style="left:614px;background:linear-gradient(135deg,#d49a5c,#b87a3e)" role="img" aria-label="Photo of dental imaging equipment used for root canals"></div>
<div class="abs svc-photo" style="left:867px;background:linear-gradient(135deg,#a89484,#5e4c40)" role="img" aria-label="Photo of the team working on a crown procedure"></div>
<div class="abs svc-label" style="left:112px">Exams &amp; Cleaning</div>
<div class="abs svc-label" style="left:364px">Tooth Colored Fillings</div>
<div class="abs svc-label" style="left:614px">Root Canals</div>
<div class="abs svc-label" style="left:867px">Crowns</div>

<section class="abs testimonials" role="img" aria-label="Photo of the office waiting room under an orange overlay"></section>
<h2 class="abs section-title testi-title">TESTIMONIALS</h2>
<p class="abs testi-quote">Well, ever since we started coming here they have given us such great service.&nbsp; I am beyond happy with all of the work that has been done to me, I loved it. That is something the other dentists were never able to do for me. Thank you so much!</p>
<div class="abs testi-name">ELENA MARSH</div>
<div class="abs testi-dots">
  <span class="dot-btn"><svg width="6" height="8" viewBox="0 0 6 8"><path d="M4.5 1L1.5 4l3 3" stroke="#ec8a34" stroke-width="1.5" fill="none"/></svg></span>
  <span class="dot-btn"><svg width="6" height="8" viewBox="0 0 6 8"><path d="M1.5 1l3 3-3 3" stroke="#ec8a34" stroke-width="1.5" fill="none"/></svg></span>
</div>

<section class="abs quote-band" role="img" aria-label="Dim photo of the office waiting area chairs"></section>
<svg class="abs quote-mark" width="50" height="42" viewBox="0 0 50 42"><path d="M0 42V22C0 10 6 3 18 0l2 5c-7 2-10 6-10 12h10v25zM28 42V22C28 10 34 3 46 0l2 5c-7 2-10 6-10 12h10v25z" fill="#8a8a8a"/></svg>
<p class="abs quote-text">The toothbrush doesn't remove six months of tartar 30 minutes before your appointment.</p>

<footer>
  <h3 class="abs foot-head" style="left:110px">QUICK LINKS</h3>
  <ul class="abs foot-links" style="left:110px"><li>Our Team</li><li>Reviews</li><li>Services</li><li>Contact Us</li><li>About</li></ul>
  <ul class="abs foot-links" style="left:256px"><li>News</li><li>Privacy Policy</li><li>Terms &amp; Conditions</li><li>Sitemap</li></ul>
  <div class="abs foot-sep" style="left:408px"></div>
  <h3 class="abs foot-head" style="left:445px">CONTACT US</h3>
  <svg class="abs" style="left:445px;top:2064px" width="20" height="28" viewBox="0 0 10 14"><path d="M5 0a5 5 0 0 0-5 5c0 4 5 9 5 9s5-5 5-9a5 5 0 0 0-5-5zm0 7a2 2 0 1 1 0-4 2 2 0 0 1 0 4z" fill="#ec8a34"/></svg>
  <div class="abs foot-org">Bayside Dental Care</div>
  <div class="abs foot-line" style="top:2088px">4820 W Harbor Ave, Millbrook, CA 95012</div>
  <svg class="abs" style="left:444px;top:2130px" width="24" height="24" viewBox="0 0 24 24"><rect width="24" height="24" rx="4" fill="#ec8a34"/><path d="M7 5l3 3.5-1.5 2a9 9 0 0 0 5 5l2-1.5 3.5 3-2 2C10 19 5 14 5 7z" fill="#fff"/></svg>
  <div class="abs foot-line" style="top:2128px">Telephone:&nbsp; 555-014-2298</div>
  <div class="abs foot-line" style="top:2153px">Mail : info@baysidedental.example</div>
  <div class="abs foot-sep" style="left:720px"></div>
  <h3 class="abs foot-head" style="left:760px">MEMBER OF</h3>
  <div class="abs badge" style="left:763px;top:2064px;width:122px;height:35px"></div>
  <div class="abs badge" style="left:928px;top:2049px;width:80px;height:50px"></div>
  <div class="abs badge" style="left:763px;top:2133px;width:77px;height:46px"></div>
</footer>

<div class="abs bottom-bar"></div>
<div class="abs copyright">Copyright©2016 Bayside Dental Care. All Right Reserved.</div>
<div class="abs social"><span></span><span></span><span></span></div>

</body>
</html>
```